RLT Nursing Care

I am a registered nurse with a private nursing care service.
We provide the following care;
Registered Nursing, Palliative Nursing, personal care, dementia repite, day respite , overnight respite, domestic assistance, welfare checks, and transport.
In the community, our service is brochured by service providers and we also supply to private clients.

Target Market(s)

Aged care, disabled clients, dementia clients in the community

Industry/Entity Type

Nurse

Font styles to use
Sans Serif

Colors
6b449b
e44699
b868aa

Requirements
Must have
• Contact: Marlene Hobbs - Registered Nurse
PO Box 482 Dubbo
0437 215 608
Nice to have
• A soft caring picture feature

```html
<!DOCTYPE html>
<html lang="en">
<head>
<meta charset="utf-8">
<title>Nursing Care Service – Postcard</title>
<link href="https://fonts.googleapis.com/css2?family=Montserrat:wght@300;400;500;600;700;800&display=swap" rel="stylesheet">
<style>
  :root {
    --violet: #6b449b;
    --magenta: #e44699;
    --orchid: #b868aa;
    --white: #ffffff;
    --backdrop: #2a2a2a;
    --stamp-line: #d9d9d9;
    --photo-green: #8fae6a;
    --photo-blue: #4a6fae;
  }
  * { margin: 0; padding: 0; box-sizing: border-box; }
  html, body {
    width: 855px; height: 1200px; overflow: hidden;
    background: var(--backdrop);
    font-family: "Montserrat", Arial, sans-serif;
  }
  .canvas { position: relative; width: 855px; height: 1200px; }

  /* Front */
  .card-front {
    position: absolute; left: 111px; top: 73px;
    width: 626px; height: 484px;
    background: var(--white); overflow: hidden;
  }
  .card-front .photo-area { position: absolute; left: 0; top: 0; }
  .call-now {
    position: absolute; right: 0; top: 38px;
    width: 261px; height: 77px;
    background: var(--orchid);
    border-radius: 12px 0 0 12px;
    color: var(--white);
    padding: 8px 0 0 34px;
    font-weight: 500;
  }
  .call-now .label { font-size: 31px; line-height: 33px; letter-spacing: 0.5px; }
  .call-now .number { font-size: 28px; line-height: 32px; letter-spacing: 0.5px; }
  .headline {
    position: absolute; left: 0; right: 0; top: 334px;
    text-align: center; color: var(--orchid);
    font-weight: 800; text-transform: uppercase;
  }
  .headline .main { display: block; font-size: 75px; line-height: 78px; letter-spacing: 1px; }
  .headline .sub { display: block; font-size: 47px; line-height: 50px; letter-spacing: 1px; font-weight: 700; }

  /* Back */
  .card-back {
    position: absolute; left: 114px; top: 604px;
    width: 621px; height: 480px;
    background: var(--white); overflow: hidden;
  }
  .card-back .panel { position: absolute; left: 0; top: 0; }
  .contact { position: absolute; left: 46px; top: 26px; color: var(--white); }
  .contact .name { font-size: 17px; font-weight: 700; letter-spacing: 0.6px; text-transform: uppercase; line-height: 20px; }
  .contact .role { font-size: 11px; font-weight: 500; letter-spacing: 3.2px; text-transform: uppercase; margin-top: 3px; line-height: 14px; }
  .contact .address { font-size: 17px; font-weight: 400; margin-top: 5px; line-height: 22px; }
  .services { position: absolute; left: 45px; top: 119px; color: var(--white); }
  .services h2 {
    font-size: 19px; font-weight: 500; line-height: 28px;
    letter-spacing: 0.5px; text-transform: uppercase;
  }
  .services ul { list-style: none; margin: 6px 0 0 -14px; }
  .services li {
    font-size: 14.5px; font-weight: 300; line-height: 24.7px;
    padding-left: 14px; position: relative;
  }
  .services li::before {
    content: ""; position: absolute; left: 0; top: 10px;
    width: 6px; height: 6px; border-radius: 50%;
    border: 1px solid var(--magenta);
  }
  .phone-pill {
    position: absolute; left: 22px; top: 418px;
    width: 181px; height: 31px;
    border: 2px solid var(--white); border-radius: 16px;
    display: flex; align-items: center; overflow: hidden;
  }
  .phone-pill .icon { width: 34px; display: flex; justify-content: center; }
  .phone-pill .number {
    flex: 1; height: 100%; background: var(--white);
    color: var(--violet); font-weight: 700; font-size: 17px;
    display: flex; align-items: center; padding-left: 8px;
  }
  .stamp-box {
    position: absolute; left: 466px; top: 16px;
    width: 138px; height: 138px;
    border: 4px solid var(--stamp-line);
  }
</style>
</head>
<body>
<div class="canvas">

  <section class="card-front">
    <svg class="photo-area" width="626" height="340" viewBox="0 0 626 340">
      <defs>
        <linearGradient id="photoTone" x1="0" y1="0" x2="1" y2="0">
          <stop offset="0" stop-color="#5aa9dc"/>
          <stop offset="0.45" stop-color="#4a6fae"/>
          <stop offset="1" stop-color="#8fae6a"/>
        </linearGradient>
      </defs>
      <path role="img" aria-label="Photo: a carer in blue scrubs pushing an elderly man in a wheelchair through a garden"
            d="M0 0 H626 V250 Q330 330 0 268 Z" fill="url(#photoTone)"/>
      <path d="M0 268 Q330 330 626 250" fill="none" stroke="#b868aa" stroke-width="5"/>
    </svg>
    <div class="call-now">
      <div class="label">CALL NOW</div>
      <div class="number">0437 215 608</div>
    </div>
    <h1 class="headline">
      <span class="main">Nursing</span>
      <span class="sub">Care Service</span>
    </h1>
  </section>

  <section class="card-back">
    <svg class="panel" width="320" height="480" viewBox="0 0 320 480">
      <path d="M0 0 H238 C330 110 320 330 188 480 H0 Z" fill="#e44699"/>
      <path d="M0 104 H274 C296 200 284 370 178 480 H0 Z" fill="#b868aa"/>
    </svg>
    <div class="contact">
      <div class="name">Marlene Hobbs</div>
      <div class="role">Registered Nurse</div>
      <div class="address">PO Box 482 Dubbo</div>
    </div>
    <div class="services">
      <h2>We provide the<br>following care:</h2>
      <ul>
        <li>Registered Nursing</li>
        <li>Palliative Nursing</li>
        <li>Personal care</li>
        <li>Dementia repite</li>
        <li>Day respite</li>
        <li>Overnight respite</li>
        <li>Domestic assistance</li>
        <li>Welfare checks</li>
        <li>Transport</li>
      </ul>
    </div>
    <div class="phone-pill">
      <span class="icon">
        <svg width="18" height="18" viewBox="0 0 24 24" aria-hidden="true">
          <path fill="#fff" d="M6.6 10.8a15.1 15.1 0 0 0 6.6 6.6l2.2-2.2a1 1 0 0 1 1-.25 11.4 11.4 0 0 0 3.6.57 1 1 0 0 1 1 1V20a1 1 0 0 1-1 1A17 17 0 0 1 3 4a1 1 0 0 1 1-1h3.5a1 1 0 0 1 1 1c0 1.25.2 2.45.57 3.570a1 1 0 0 1-.25 1z"/>
        </svg>
      </span>
      <span class="number">0437 215 608</span>
    </div>
    <div class="stamp-box"></div>
  </section>

</div>
</body>
</html>
```